Vorna Electric Construction We Light It Up!

We have an up coming meeting with a developer and general contractor. This card must bring out the best in my business. My business is an up and coming MDBE certified electrical contactor. I need a very powerful card to represent me business that we be bold and represent what I am about. WE LIGHT IT UP!

Target Market(s)

General Contractors, developers and property owners

Industry/Entity Type

Electrical

Contact Information for Business Card

great card that really brings out my bussiness

Colors
0355a3
3276b5
0393ce
34a6d7

Requirements
Must have
• Great design
Nice to have
• very different and noticeable card
Should not have
• open to anything

```html
<!DOCTYPE html>
<html lang="en">
<head>
<meta charset="utf-8">
<title>Vorna Electric Construction – Business Card</title>
<link rel="stylesheet" href="https://fonts.googleapis.com/css2?family=Arimo:wght@400&family=Montserrat:wght@400;500&display=swap">
<style>
  :root{
    --stage:#2e2f31;
    --paper:#f4f5f7;
    --paper-shade:#e8eaee;
    --brand-deep:#0355a3;
    --brand-mid:#3276b5;
    --brand-bright:#0393ce;
    --brand-sky:#34a6d7;
    --band:#3ea0d2;
    --ink-light:#ffffff;
  }
  html,body{margin:0;padding:0;width:1200px;height:884px;overflow:hidden;background:var(--stage);}
  .stage{position:relative;width:1200px;height:884px;}
  .card{position:absolute;width:540px;height:310px;top:287px;background:var(--paper);overflow:hidden;box-shadow:0 6px 18px rgba(0,0,0,.45);}
  .card--back{left:40px;}
  .card--front{left:620px;}
  .card__shapes{position:absolute;inset:0;}
  .wordmark{position:absolute;display:flex;align-items:center;gap:10px;font-family:"Arimo",Arial,sans-serif;font-weight:400;color:var(--brand-bright);white-space:nowrap;}
  .wordmark__square{display:block;background:var(--brand-deep);}
  .card--back .wordmark{left:150px;top:128px;font-size:24px;}
  .card--back .wordmark__square{width:22px;height:22px;}
  .card--front .wordmark{left:28px;top:62px;font-size:19px;}
  .card--front .wordmark__square{width:16px;height:16px;}
  .contact{position:absolute;left:34px;top:138px;font-family:"Montserrat",sans-serif;color:var(--ink-light);}
  .contact__name{margin:0;font-size:27px;font-weight:500;line-height:1;}
  .contact__role{margin:2px 0 16px 6px;font-size:14px;line-height:1.1;}
  .contact__list{list-style:none;margin:0;padding:0;}
  .contact__item{display:flex;align-items:flex-start;gap:9px;font-size:15px;line-height:1.05;margin-bottom:9px;}
  .contact__icon{flex:none;width:13px;height:13px;margin-top:2px;fill:var(--ink-light);}
</style>
</head>
<body>
<main class="stage">

  <section class="card card--back" aria-label="Card back">
    <svg class="card__shapes" viewBox="0 0 540 310" aria-hidden="true">
      <polygon points="0,0 540,0 540,310 0,310" fill="var(--paper)"/>
      <polygon points="0,180 120,0 160,0 110,310 0,310" fill="var(--paper-shade)" opacity=".5"/>
      <polygon points="0,110 150,40 120,310 0,310" fill="var(--brand-sky)"/>
      <polygon points="0,230 150,40 120,310 0,310" fill="var(--band)"/>
    </svg>
    <div class="wordmark"><span class="wordmark__square"></span>Vorna Electric Construction</div>
  </section>

  <section class="card card--front" aria-label="Card front">
    <svg class="card__shapes" viewBox="0 0 540 310" aria-hidden="true">
      <polygon points="0,0 540,0 540,310 0,310" fill="var(--paper)"/>
      <polygon points="0,118 540,28 540,292 0,292" fill="var(--band)"/>
      <polygon points="220,0 540,0 480,60" fill="var(--brand-sky)"/>
      <polygon points="470,0 540,0 540,310 300,310" fill="var(--brand-mid)"/>
      <polygon points="505,0 540,0 540,310 380,310" fill="var(--brand-deep)" opacity=".55"/>
    </svg>
    <div class="wordmark"><span class="wordmark__square"></span>Vorna Electric Construction</div>
    <div class="contact">
      <h1 class="contact__name">Dean Marlow</h1>
      <p class="contact__role">Dirctor</p>
      <ul class="contact__list">
        <li class="contact__item">
          <svg class="contact__icon" viewBox="0 0 16 16"><path d="M8 1 1 7.5h2V15h4v-4h2v4h4V7.5h2z"/></svg>
          <span>42 Harbour Lane Eastfield VIC<br>3990 Australia</span>
        </li>
        <li class="contact__item">
          <svg class="contact__icon" viewBox="0 0 16 16"><path d="M4 1l2.5 3-1.5 2c1 2 3 4 5 5l2-1.5 3 2.5-1.5 2.5C7 14.5 1.5 9 1.5 2.5z"/></svg>
          <span>+61 400 555 019</span>
        </li>
        <li class="contact__item">
          <svg class="contact__icon" viewBox="0 0 16 16"><path d="M1 3h14v10H1z M1 3l7 6 7-6" stroke="var(--band)" stroke-width="1.2"/></svg>
          <span>hello@vornaelectric.com.au</span>
        </li>
      </ul>
    </div>
  </section>

</main>
</body>
</html>
```